**** Business card design for VoltaNode ****

For my ICT company VoltaNode I need I need a business card design.

We design, build and host web-applications and we have our own CMS product.

Some good examples are attached.

The information should be:
Joris Tielenburg
Managing director
E: j.tielenburg@voltanode-example.nl
M: +31(0)6 57218064
T: +31(0)40 7249305
W: www.voltanode-example.nl

Address:
Berend Vlootweg 27
5612 KT Eindhoven

Industry/Entity Type

Business

Requirements
Must have
• - Use logo (see attachments)
- Double sided
- Distinctive
Nice to have
• - Place for a statement on the back-side: "Designed with knowledge, built with passion"
- HTML code (or Wordpress)
- Dark (black or dark-gray) side
- Small simple images for telephone, e-mail en Url.
- QR code (only if not disturbing), not required, just an option

```html
<!DOCTYPE html>
<html lang="en">
<head>
<meta charset="utf-8">
<title>VoltaNode business card</title>
<link rel="stylesheet" href="https://fonts.googleapis.com/css2?family=Questrial&display=swap">
<style>
  :root {
    --stage: #dfe4e7;
    --card-white: #ffffff;
    --card-dark: #231f20;
    --ink-dark: #1c2430;
    --ink-light: #f2f2f2;
    --blue: #4a8fd8;
    --blue-soft: #a9cdf0;
    --blue-pale: #d9eaf9;
    --dot: #4a8fd8;
  }
  * { box-sizing: border-box; margin: 0; padding: 0; }
  html, body { width: 1200px; height: 960px; overflow: hidden; }
  body {
    background: var(--stage);
    font-family: "Questrial", "Century Gothic", sans-serif;
    position: relative;
  }
  .card {
    position: absolute;
    left: 215px;
    width: 770px;
    height: 440px;
    overflow: hidden;
    box-shadow: 0 6px 22px rgba(0,0,0,.18);
  }
  .card--front { top: 30px; background: var(--card-white); }
  .card--back { top: 490px; background: var(--card-dark); color: var(--ink-light); }

  /* front */
  .front__wordmark {
    position: absolute; left: 40px; top: 95px; width: 690px;
    text-align: center; white-space: nowrap;
    font-size: 118px; font-weight: 400; letter-spacing: 2px; color: var(--ink-dark);
    line-height: 1;
  }
  .front__band {
    position: absolute; left: 0; bottom: 40px; width: 540px; height: 48px;
    background: linear-gradient(90deg, var(--blue) 0%, var(--blue-soft) 70%, var(--blue-pale) 100%);
  }
  .front__url-box {
    position: absolute; left: 80px; bottom: 66px; width: 450px; height: 44px;
    border-radius: 6px;
    background: linear-gradient(90deg, var(--blue-pale), var(--blue-soft));
    display: flex; align-items: center; justify-content: center;
    white-space: nowrap;
    font-size: 22px; letter-spacing: 1px; color: var(--ink-dark);
  }
  .front__brand {
    position: absolute; right: 40px; bottom: 80px;
    display: flex; align-items: center; gap: 10px; white-space: nowrap;
    font-size: 30px; color: var(--ink-dark);
  }
  .brand-dot { width: 40px; height: 40px; border-radius: 50%; background: var(--blue); flex: none; }

  /* back */
  .bullet::before {
    content: ""; display: inline-block; width: 7px; height: 7px; border-radius: 50%;
    background: var(--dot); margin-right: 8px; vertical-align: middle; position: relative; top: -2px;
  }
  .back__person { position: absolute; left: 38px; top: 36px; white-space: nowrap; }
  .back__name { font-size: 30px; letter-spacing: 2px; font-weight: 400; }
  .back__role { font-size: 20px; letter-spacing: 1.5px; margin-left: 15px; }
  .back__brand {
    position: absolute; right: 50px; top: 50px;
    display: flex; align-items: center; gap: 10px; white-space: nowrap;
    font-size: 24px; color: var(--ink-light);
  }
  .back__brand .brand-dot { width: 54px; height: 54px; }
  .back__contacts { position: absolute; left: 50px; top: 210px; list-style: none; white-space: nowrap; font-size: 18px; letter-spacing: .5px; line-height: 1.3; }
  .back__contacts .gap { margin-top: 22px; }
  .back__address { position: absolute; right: 40px; top: 232px; font-style: normal; white-space: nowrap; font-size: 18px; letter-spacing: .5px; line-height: 1.3; }
  .back__address span { display: block; }
  .back__address .indent { margin-left: 15px; }
  .back__url {
    position: absolute; right: 0; top: 300px; width: 390px; height: 34px;
    border-radius: 5px 0 0 5px;
    background: linear-gradient(90deg, var(--blue-pale), var(--blue-soft) 45%, var(--blue));
    display: flex; align-items: center; justify-content: center; white-space: nowrap;
    font-size: 19px; letter-spacing: 1.5px; color: var(--ink-dark);
  }
</style>
</head>
<body>
  <section class="card card--front" aria-label="Card front">
    <h1 class="front__wordmark">VoltaNode</h1>
    <div class="front__band"></div>
    <div class="front__url-box">www.voltanode-example.com</div>
    <div class="front__brand"><span class="brand-dot"></span><span>VoltaNode</span></div>
  </section>

  <section class="card card--back" aria-label="Card back">
    <div class="back__person">
      <h2 class="back__name bullet">Joris Tielenburg</h2>
      <p class="back__role">Managing director</p>
    </div>
    <div class="back__brand"><span class="brand-dot"></span><span>VoltaNode</span></div>
    <ul class="back__contacts">
      <li class="bullet">+31(0)6 57218064</li>
      <li class="bullet">+31(0)40 7249305</li>
      <li class="bullet gap">j.tielenburg@voltanode-example.nl</li>
    </ul>
    <address class="back__address">
      <span class="bullet">Berend Vlootweg 27</span>
      <span class="indent">5612 KT Eindhoven</span>
    </address>
    <div class="back__url">www.voltanode-example.com</div>
  </section>
</body>
</html>
```